Brochure layout for a small country church

St. Wendel is a small country church located on the central coast of CA. Last year our priest retired, and we are in the process of seeking a new church leader. To support our search process, we created a profile brochure that describes who we are in words and images.

The copy has been carefully written and fully edited, and we have gathered, tagged and foldered high-resolution images. We now need a person with your talents to arrange the words and pictures for us!

This document, which we call a 'profile' but is actually a brochure, will be in PDF format, size 8.5x11, for web display and local printing only. It will be posted on a national database and be shared with candidates by email and on our website. We do not intend to reproduce this on paper, though we expect some users will print pages on their printers.

Here is a Cloudpail link to access the copy, images and layout instructions:
https://www.cloudpail-share.net/sh/k3rtezn7wqa8u2x/BBDQLM-17h88_pR4TUwnXoEbz

The layout instructions include specific information on image placement, and gives you much flexibility to arrange the copy/images the way you think looks best. All we ask is that you do not change the copy.

Images may be processed, cropped, inverted, enhanced … whatever you think looks right. We tried to give you the largest images possible, so you can get good resolution on the page.

Please do not let the length of the document concern you … you can cut/paste the copy, using any serif font that matches the look/feel of our church, and all of the images have been tagged and folder addressed in the document so you know where to find them. Page count does not matter as long as it looks good, and once you start laying out the pages it should not take long to finish. We just need someone with your design skills to make it look good!

As we stated in the copy narrative, we are a warm, loving and inclusive parish that is humble, happy and grateful for the many blessings we have. Our greatest quality is our people. In your design work, anything you can do to bring forward these values will be appreciated.

If you have any questions, please do not hesitate to contact me (Gordon Pelley/gordon@gordonpelley-mail.net) and I will answer them for you right away.

Thank you for considering our brochure project, and we look forward to your submission.

Industry/Entity Type

Church

```html
<!DOCTYPE html>
<html lang="en">
<head>
<meta charset="utf-8">
<title>Our Community</title>
<link rel="stylesheet" href="https://fonts.googleapis.com/css2?family=EB+Garamond:wght@400;500&display=swap">
<style>
  :root {
    --page: #ffffff;
    --ink: #1a1a1a;
    --rule: #1a1a1a;
    --link: #2f6fb7;
    --photo-sky: #d9d6c4;
    --photo-oak: #6f6a44;
    --photo-grass: #8f7f58;
    --photo-ground: #6a5a3e;
  }
  * { margin: 0; padding: 0; box-sizing: border-box; }
  html, body {
    width: 1200px;
    height: 928px;
    overflow: hidden;
    background: var(--page);
  }
  .page {
    position: relative;
    width: 1200px;
    height: 928px;
    background: var(--page);
    color: var(--ink);
    font-family: "EB Garamond", Garamond, Georgia, serif;
  }
  .section-title {
    position: absolute;
    left: 52px;
    top: 46px;
    width: 538px;
    font-size: 23px;
    font-weight: 400;
    line-height: 1.2;
    padding-bottom: 1px;
    border-bottom: 1.5px solid var(--rule);
  }
  .community-photo {
    position: absolute;
    left: 0;
    top: 100px;
    width: 1200px;
    height: 433px;
    background:
      linear-gradient(180deg, var(--photo-sky) 0%, #b4b08c 18%, var(--photo-oak) 38%, #7d7560 60%, var(--photo-grass) 78%, var(--photo-ground) 100%);
  }
  .body-copy {
    position: absolute;
    left: 52px;
    top: 548px;
    width: 1098px;
    height: 330px;
    column-count: 2;
    column-gap: 22px;
    column-fill: auto;
    font-size: 15.2px;
    line-height: 26.3px;
    text-align: justify;
    hyphens: auto;
  }
  .body-copy p { margin-bottom: 3px; }
  .body-copy a { color: var(--link); text-decoration: none; }
  .page-number {
    position: absolute;
    left: 0;
    width: 1200px;
    top: 898px;
    text-align: center;
    font-size: 11px;
    font-weight: 500;
  }
</style>
</head>
<body>
<main class="page">
  <h1 class="section-title">Our Community</h1>

  <div class="community-photo" role="img" aria-label="Group photo of about twenty parishioners standing together outdoors under oak trees on dry grass"></div>

  <div class="body-copy">
    <p>Cattle ranching. Hay farming. Vineyards. Aerospace manufacturing. Software development. Shopping. Good schools. We have it all–a rich history woven into a vibrant contemporary culture.</p>
    <p>Our city is El Paso de Robles (“Pass of the Oaks”), organized in 1889, overlooking the upper Salinas River, conveniently located midway between San Francisco and Los Angeles. Our community is a mix of local families that have been here for generations, retirees from urban centers north and south of the area, young families seeking a great community in which to raise their children, and immigrants seeking opportunities for a better life.</p>
    <p>City life revolves around a grand central park with an historic Hartwell library, a modern movie theater, award-winning restaurants and gathering places. Our city calendar is filled with family-friendly events, with both modern festivals and traditional celebrations that echo Paso’s pioneer roots.</p>
    <p>The San Luis Obispo-Paso Robles MSA (Metropolitan Statistical Area) ranked second most satisfied in the US on a recent Brightline-Vitality Well Being Index. We also ranked 8 out of 189 metropolitan areas in overall well being.</p>
    <p>In recent years viticulture and winemaking has become more prominent, with Paso Robles being named “Wine Region of the Year” for 2013 by Vintner’s Table Magazine. The 270-plus wineries and a superior group of restaurants have led to a vibrant wine tourism industry. Paso Robles has been noted as a top vacation destination by the WayfarerPost and The Daily Ledger.</p>
    <p>For more information on the city of Paso Robles and surrounding communities, please visit our website at <a href="#">www.stwendel-parish.org/rector.html</a>.</p>
  </div>

  <div class="page-number">8</div>
</main>
</body>
</html>
```